Flyer Design - High Quality

*** Although this current job contest is listed as a ‘one-off contest’ we are also looking at working with a graphic designer long-term, which will include quite regular design work. So even though this is just a small job, if you want to & you do a good job on this, we would love to look at working with you on a regular basis.
* The winning designer will also get a freelance job designing another flyer in same design
Job Basics:
1. the design of a ….
Promotional corporate flyer - size = A4 - approx 6 or 7 pages.
*** The design will need to be extremely high quality/professional. Must be of a similar or better standard as the attached flyers – 1) Ross Penley_Info Pack & 2) DrGlen Whitcombe
* Please view these flyers first to ensure you can create a flyer of similar or better quality before proceeding.
Specific Requirements:
1. high-quality, professional promotional flyer [size = A4 - for online use predominantly . I.e. not for printing necessarily] using the text, images and basic instructions outlined on the word document attached - 'Flyer_All talks in 1_guidelines'.
2. Examples of similar quality (good) designs = 1) Ross Penley_Info Pack & 2) DrGlen Whitcombe
Background:
I am a motivational speaker on health, well-being and work-life balance. This flyer is to be used for promotional purposes when clients inquire about me speaking at their conference. Ross Penley & Glen Whitcombe are speakers who do somewhat similar talks to me, and who have flyers that I really like.
Theme: My general theme is ‘health and well-being’ (we're a little bit more towards natural health and Eastern medicine, but don't want it too ‘eastern’ if you know what I mean).
Main Look & Feel … to be conveyed:
Professional / Corporate
Health, Vitality and happiness (fresh, modern and vital)
eye-catching / attention grabbing
* The design should represent a balance between highly sophisticated, professional and classy - corporate savvy - with a hint of 'natural health, Eastern wisdom and a general ‘high energy/fresh health and vitality feel'. While we would like the design to convey some aspect of ‘ natural/Eastern’ wisdom), we predominantly want to convey the idea of ‘modern’ health (i.e. fresh, modern and vital).
Colours:
We are open to your creative suggestions, but were generally thinking something along the lines of the colours in our corporate logo –
dark blue, aqua blue, grey – see logo (KVT_300kb.jpg) in attachments
- possibly with some bright green, orange etc if you think it might suit – to help give it the ‘natural health’ feel.
* Notes:
1. SAVING YOUR TIME: If you just want to start just doing a quickish design of the first 1-2 pages and submitting that (images for these pages attached - though use own images if you think they are better), then that’s fine. Then we can let you know if it is along the lines of something we like or not. This way, you can do something relatively quickly, without wasting too much time, if it is definitely not something we like. Hope that helps - we are always conscious of trying to make things good for you as a designer too.
2. Do not feel completely bound to the ideas suggested/asked for. Feel free to convey the basic ideas/keys but feel free to use/follow some of your own ideas/creative desires.
3. Any photos/images should be royalty free (or ask us if we want to pay for it) and not widely used or seen in the public domain - i.e. we don’t want people to have seen the photo/image elsewhere (within reason).
Thanks a lot and look forward to receiving your first design!
Cheers
Owen
Target Market(s)
Predominantly corporates / business groups.
Industry/Entity Type
Graphic Designer

```html
<!DOCTYPE html>
<html lang="en">
<head>
<meta charset="utf-8">
<title>Speaker Flyer – Owen Harlow</title>
<link rel="stylesheet" href="https://fonts.googleapis.com/css2?family=Squada+One&family=Varela+Round&family=Raleway:wght@400;700&display=swap">
<style>
  :root {
    --paper: #ffffff;
    --aqua: #1fa3bb;
    --teal-deep: #1a7390;
    --navy: #1e3c6a;
    --grey: #6d7378;
    --crowd-a: #4a4038;
    --crowd-b: #8a6f5c;
    --crowd-c: #2d2a2c;
    --speaker-a: #9aa2a6;
    --speaker-b: #4d5257;
  }
  * { margin: 0; padding: 0; box-sizing: border-box; }
  html, body { width: 851px; height: 1200px; overflow: hidden; background: var(--paper); }
  .flyer { position: relative; width: 851px; height: 1200px; background: var(--paper); overflow: hidden; }

  .crowd-photo {
    position: absolute; left: 0; top: 0; width: 851px; height: 470px;
    background: radial-gradient(ellipse at 60% 55%, var(--crowd-b) 0%, var(--crowd-a) 45%, var(--crowd-c) 100%);
  }
  .speaker-photo {
    position: absolute; left: 14px; top: 335px; width: 228px; height: 340px;
    background: linear-gradient(160deg, var(--speaker-a) 0%, var(--speaker-b) 100%);
    border: 4px solid var(--paper);
  }

  .headline {
    position: absolute; left: 252px; top: 492px; width: 595px;
    font-family: "Squada One", sans-serif; font-weight: 400; font-size: 62px; line-height: 62px;
    text-transform: uppercase; letter-spacing: 1px; color: var(--aqua);
  }

  .topic {
    position: absolute; font-family: "Varela Round", sans-serif;
    font-size: 53px; color: var(--teal-deep); white-space: nowrap;
  }
  .topic-health { left: 24px; top: 722px; }
  .topic-motivation { left: 250px; top: 826px; }
  .topic-balance { left: 350px; top: 920px; }

  .brand { position: absolute; left: 26px; top: 1078px; display: flex; align-items: center; gap: 12px; }
  .brand-mark { width: 40px; height: 40px; flex: none; }
  .brand-text { display: flex; flex-direction: column; }
  .brand-name {
    font-family: "Raleway", sans-serif; font-weight: 700; font-size: 33px;
    letter-spacing: 1px; color: var(--navy); line-height: 1;
  }
  .brand-tagline {
    font-family: "Raleway", sans-serif; font-weight: 400; font-size: 10px;
    letter-spacing: 1px; color: var(--navy); margin-top: 6px; text-transform: uppercase;
    white-space: nowrap;
  }

  .testimonial {
    position: absolute; left: 380px; top: 1112px;
    font-family: "Raleway", sans-serif; font-size: 17px; letter-spacing: 0.5px;
    color: var(--grey); white-space: nowrap;
  }
</style>
</head>
<body>
<main class="flyer">
  <div class="crowd-photo" role="img" aria-label="Conference audience standing with arms raised, smiling and energised"></div>
  <div class="speaker-photo" role="img" aria-label="Speaker presenting on stage, gesturing to the audience"></div>

  <h1 class="headline">Looking for an<br>entertaining high<br>motivation speaker on</h1>

  <p class="topic topic-health">health &amp; wellbeing ...</p>
  <p class="topic topic-motivation">motivation ...</p>
  <p class="topic topic-balance">work-life balance?</p>

  <div class="brand">
    <svg class="brand-mark" viewBox="0 0 40 40" aria-hidden="true">
      <circle cx="20" cy="20" r="18" fill="var(--aqua)"/>
    </svg>
    <div class="brand-text">
      <span class="brand-name">OWEN HARLOW</span>
      <span class="brand-tagline">Health Wellbeing Work-Life Balance</span>
    </div>
  </div>

  <p class="testimonial">“…inspirational” – Southern Coast Bank</p>
</main>
</body>
</html>
```